Football and Sports Management Agency Stationary

We have a logo, fonts, website and colour palette.
We need the logo refined by a proper designer and then business stationary designed. You can see on the website how it needs adjusting by a designers eye.
The company is a high end sports management company aiming to attract and represent professional athletes. The name Velorin is to indicate a 'Constellation of Stars' ie our clients. The dots on the star should be slightly different sizes to reflect that some clients will be bigger than others.
Colours:
#e6e6e6
#edd2a4
#caaa72 (main gold and also used on site)
#3f3f42
#001d38
#edeced (on website)
#191c23 (on website)
Font:
QT (velorin)
QT Melbrook (sports management)
We would like:
- Letterhead (word and indesign and PDF print format). I have attached an example for one I like. It's quiet a clean design with the contact details and address taking up only a small amount of room.
- Business card (dark on the back with the logo, personal details on the front). Only needs name, title, email, website and phone number. No company address (in PDF and indesign format)
- Powerpoint slide theme
- Logo in vector format for light and dark versions and single colour versions. And optimised web version
- Simple brand guide PDF showing colour, font and logo (a one/two page PDF)
Any questions, please ask.
NEW INFO:
Contact Details
Maren Solwick
Director
Mobile: +44 7630 218 977
Phone: +44 0113 872 604
Email: maren@velorinathletic.example
Web: velorinathletic.example
Corran Lodge, 14 Mill Bank Road, Stockport, SK4 9TW
Company number 40718362
Target Market(s)
Professional athletes, professional sports teams.
Industry/Entity Type
Management
Requirements
Must have
- NEW
- The designs must look cool, classy and high quality. My suggestion for this is to keep the text small and precise with uncomplicated design.
Nice to have
- Application of brand displayed on stationary and additional pieces of stationary branded.
- Draw some inspiration from the website. eg the slant angles used separate the sections.
Should not have
- Don't create new logos etc.

```html
<!DOCTYPE html>
<html lang="en">
<head>
<meta charset="utf-8">
<title>Velorin Sports Management – Stationery</title>
<link href="https://fonts.googleapis.com/css2?family=Josefin+Sans:wght@300&family=Questrial&family=Oswald:wght@600&display=swap" rel="stylesheet">
<style>
  :root {
    --board: #3d3d3e;
    --paper: #ffffff;
    --ink: #3f3f42;
    --navy: #191c23;
    --gold: #caaa72;
    --gold-light: #edd2a4;
    --muted: #e6e6e6;
  }
  * { box-sizing: border-box; margin: 0; padding: 0; }
  html, body { width: 1200px; height: 1200px; overflow: hidden; }
  body { background: var(--board); position: relative; font-family: "Questrial", sans-serif; color: var(--ink); }

  .wordmark { font-family: "Josefin Sans", sans-serif; font-weight: 300; letter-spacing: .42em; text-transform: uppercase; white-space: nowrap; }

  /* Letterhead */
  .letterhead { position: absolute; left: 110px; top: 246px; width: 474px; height: 673px; background: var(--paper); box-shadow: 0 10px 18px rgba(0,0,0,.35); }
  .letterhead > * { position: absolute; }
  .lh-logo { left: 58px; top: 64px; display: flex; align-items: center; gap: 8px; }
  .lh-logo .dot { width: 6px; height: 6px; border-radius: 50%; background: var(--gold); }
  .lh-logo .wordmark { font-size: 13px; color: var(--ink); }
  .lh-contact { left: 338px; top: 57px; font-size: 5px; line-height: 9.4px; list-style: none; }
  .lh-contact li { display: flex; align-items: center; gap: 5px; }
  .lh-contact svg { width: 5px; height: 5px; fill: var(--gold); }
  .lh-address { left: 58px; top: 149px; font-size: 7.2px; line-height: 9.6px; }
  .lh-date { left: 58px; top: 225px; font-size: 7.2px; }
  .lh-greeting { left: 58px; top: 280px; font-size: 7.2px; }
  .lh-greeting span { display: inline-block; width: 30px; border-bottom: .6px solid var(--ink); }
  .lh-body { left: 58px; width: 351px; font-size: 7.4px; line-height: 9.6px; text-align: justify; }
  .lh-from { left: 58px; top: 491px; font-size: 7.2px; }
  .lh-signature { left: 60px; top: 520px; width: 100px; height: 20px; background: linear-gradient(90deg, rgba(74,66,150,.12), rgba(74,66,150,.25)); border-radius: 3px; }
  .lh-signline { left: 58px; top: 542px; width: 130px; border-top: .6px solid #777; }

  /* Business cards */
  .card { position: absolute; left: 550px; width: 201px; height: 114px; background: var(--navy); box-shadow: -4px 8px 14px rgba(0,0,0,.35); color: #fff; }
  .card-front { top: 464px; }
  .card-back { top: 586px; display: flex; align-items: center; justify-content: center; }
  .card-back .wordmark { font-size: 13px; color: #fff; margin-top: 12px; }
  .card-name { position: absolute; top: 29px; width: 100%; text-align: center; font-size: 5.6px; }
  .card-title { position: absolute; top: 37px; width: 100%; text-align: center; font-size: 4.4px; color: var(--gold); }
  .card-col { position: absolute; top: 52px; font-size: 3.8px; line-height: 7px; color: var(--gold); }
  .card-col.left { right: 106px; text-align: right; }
  .card-col.right { left: 112px; }
  .card-divider { position: absolute; left: 100px; top: 49px; height: 17px; border-left: .6px solid var(--gold); }
  .card-address { position: absolute; top: 74px; width: 100%; text-align: center; font-size: 3.8px; line-height: 5px; color: var(--gold-light); }

  /* Slides */
  .slide { position: absolute; left: 792px; width: 338px; height: 254px; background: var(--paper); overflow: hidden; }
  .slide-cover { top: 70px; background: var(--navy); }
  .cover-photo { position: absolute; inset: 0; background: radial-gradient(ellipse 60% 30% at 50% 55%, #3c4a3c 0%, #1e2622 55%, #12161a 100%); }
  .cover-logo { position: absolute; top: 112px; width: 100%; text-align: center; }
  .cover-logo .wordmark { font-size: 26px; color: #fff; padding-left: .42em; }
  .slide-title { position: absolute; left: 27px; top: 30px; font-family: "Oswald", sans-serif; font-weight: 600; font-size: 18px; letter-spacing: .02em; color: var(--navy); }
  .slide-rule { position: absolute; left: 27px; top: 54px; width: 283px; border-top: 1.3px solid var(--gold); }
  .slide-footer { position: absolute; left: 0; bottom: 0; width: 100%; height: 56px; }
  .slide-footer svg { position: absolute; inset: 0; }
  .slide-footer .wordmark { position: absolute; left: 42px; bottom: 18px; font-size: 10px; color: #fff; }
  .slide-footer .dot { position: absolute; left: 28px; bottom: 21px; width: 5px; height: 5px; border-radius: 50%; background: var(--gold); }
  .slide-copy { position: absolute; font-size: 4.4px; line-height: 5.5px; text-align: justify; color: var(--ink); }
  .chart { position: absolute; left: 190px; top: 58px; }
  .chart text { font-family: "Questrial", sans-serif; font-size: 7.5px; }
  .venn { position: absolute; left: 116px; top: 84px; }
  .venn text { font-family: "Questrial", sans-serif; font-size: 17px; fill: var(--gold); }
  .placeholder { position: absolute; left: 30px; top: 79px; width: 147px; height: 104px; border: 1.4px dashed var(--navy); display: flex; align-items: center; justify-content: center; }
  .placeholder-icons { display: grid; grid-template-columns: repeat(3, 9px); gap: 3px; }
  .placeholder-icons span { height: 9px; border: .6px solid #9fb6c8; background: #e6eef4; }
</style>
</head>
<body>

<!-- Letterhead -->
<section class="letterhead">
  <div class="lh-logo"><span class="dot"></span><span class="wordmark">Velorin</span></div>
  <ul class="lh-contact">
    <li><svg viewBox="0 0 10 10"><rect x="1" y="3" width="8" height="5" rx="1"/></svg>+44 0113 872 604</li>
    <li><svg viewBox="0 0 10 10"><path d="M2 1h2l1 3-1.5 1a6 6 0 0 0 2.5 2.5L7 6l3 1v2a1 1 0 0 1-1 1A8 8 0 0 1 1 2a1 1 0 0 1 1-1z"/></svg>+44 7630 218 977</li>
    <li><svg viewBox="0 0 10 10"><rect x="0" y="2" width="10" height="6" rx="1"/></svg>maren@velorinathletic.example</li>
    <li><svg viewBox="0 0 10 10"><circle cx="5" cy="5" r="4.5"/></svg>velorinathletic.example</li>
  </ul>
  <p class="lh-address">Corran Lodge, 14 Mill Bank Road,<br>Stockport, SK4 9TW<br>Company number 40718362</p>
  <p class="lh-date">DATE:3/5/2018</p>
  <p class="lh-greeting">Dear, Mr.<span></span></p>
  <p class="lh-body" style="top:312px">Lorem ipsum dolor sit amet, consectetur adipiscing elit, sed do eiusmod tempor incididunt ut labore et dolore magna aliqua. Est pellentesque elit ullamcorper dignissim cras.</p>
  <p class="lh-body" style="top:360px">Lorem ipsum dolor sit amet, consectetur adipiscing elit, sed do eiusmod tempor incididunt ut labore et dolore magna aliqua. Pharetra et ultrices neque ornare aenean euismod. Nunc eget lorem dolor sed viverra ipsum nunc. Ac ut consequat semper viverra nam libero. Eget gravida cum sociis natoque. Pretium viverra suspendisse potenti nullam. In hendrerit gravida rutrum quisque non. Ultrices gravida dictum fusce ut placerat orci. Accumsan tortor posuere ac ut consequat semper viverra. Feugiat sed lectus vestibulum mattis.</p>
  <p class="lh-body" style="top:437px">Lorem ipsum dolor sit amet, consectetur adipiscing elit, sed do eiusmod tempor incididunt ut labore et dolore magna aliqua. Non arcu risus quis varius quam quisque. Tincidunt eget nullam non nisi est sit amet. Tincidunt tortor aliquam nulla facilisi cras fermentum odio eu feugiat. Id leo in vitae turpis massa sed elementum tempus egestas.</p>
  <p class="lh-from">From: Maren Solwick ( Director )</p>
  <div class="lh-signature" role="img" aria-label="Handwritten signature"></div>
  <div class="lh-signline"></div>
</section>

<!-- Business card, front -->
<section class="card card-front">
  <p class="card-name">Maren Solwick</p>
  <p class="card-title">Director</p>
  <div class="card-col left">+44 0113 872 604<br>+44 7630 218 977</div>
  <div class="card-divider"></div>
  <div class="card-col right">maren@velorinathletic.example<br>velorinathletic.example</div>
  <p class="card-address">Corran Lodge, 14 Mill Bank Road,<br>Stockport, SK4 9TW Company number: 40718362</p>
</section>

<!-- Business card, back -->
<section class="card card-back">
  <span class="wordmark">Velorin</span>
</section>

<!-- Slide: cover -->
<section class="slide slide-cover">
  <div class="cover-photo" role="img" aria-label="Floodlit football stadium seen from the stands"></div>
  <div class="cover-logo"><span class="wordmark">Velorin</span></div>
</section>

<!-- Slide: chart -->
<section class="slide" style="top:339px">
  <h2 class="slide-title">TITLE GOES HERE</h2>
  <div class="slide-rule"></div>
  <p class="slide-copy" style="left:28px;top:65px;width:130px">Velorin guides professional athletes through contracts, sponsorship and career planning with discreet, precise support. Our team works across football and wider sport, building long term partnerships that protect value on and off the pitch. Every client receives a dedicated manager, clear reporting and steady advice at each stage of the season. Velorin guides professional athletes through contracts, sponsorship and career planning with discreet, precise support. Our team works across football and wider sport, building long term partnerships that protect value on and off the pitch. Every client receives a dedicated manager, clear reporting and steady advice at each stage of the season.</p>
  <svg class="chart" width="120" height="120" viewBox="0 0 120 120">
    <g fill="var(--navy)">
      <text x="0" y="8">5</text><text x="0" y="26">4</text><text x="0" y="43">3</text>
      <text x="0" y="61">2</text><text x="0" y="79">1</text><text x="0" y="96">0</text>
    </g>
    <rect x="26" y="53" width="15" height="39" fill="var(--navy)"/>
    <rect x="46" y="4" width="15" height="88" fill="var(--gold)"/>
    <rect x="66" y="25" width="15" height="67" fill="var(--gold)"/>
    <rect x="86" y="43" width="15" height="49" fill="var(--navy)"/>
    <rect x="106" y="25" width="14" height="67" fill="var(--gold)"/>
    <line x1="22" y1="5" x2="22" y2="92" stroke="var(--navy)" stroke-width=".6"/>
    <g fill="var(--gold)">
      <text x="30" y="117">A</text><text x="50" y="117">B</text><text x="70" y="117">C</text>
      <text x="90" y="117">D</text><text x="110" y="117">E</text>
    </g>
  </svg>
  <div class="slide-footer">
    <svg viewBox="0 0 338 56" preserveAspectRatio="none"><polygon points="0,0 338,36 338,56 0,56" fill="var(--navy)"/></svg>
    <span class="dot"></span><span class="wordmark">Velorin</span>
  </div>
</section>

<!-- Slide: diagram -->
<section class="slide" style="top:610px">
  <h2 class="slide-title">TITLE GOES HERE</h2>
  <div class="slide-rule"></div>
  <p class="slide-copy" style="left:27px;top:98px;width:83px">Short note on the first key point, kept brief and clear for the slide.</p>
  <p class="slide-copy" style="left:27px;top:142px;width:83px">Short note on the second key point, kept brief and clear for the slide.</p>
  <p class="slide-copy" style="left:232px;top:98px;width:83px">Short note on the third key point, kept brief and clear for the slide.</p>
  <p class="slide-copy" style="left:232px;top:142px;width:83px">Short note on the fourth key point, kept brief and clear for the slide.</p>
  <svg class="venn" width="110" height="100" viewBox="0 0 110 100">
    <g fill="var(--navy)" fill-opacity=".94" stroke="#0d0f14" stroke-width="1">
      <circle cx="54" cy="32" r="29"/>
      <circle cx="34" cy="62" r="29"/>
      <circle cx="74" cy="62" r="29"/>
    </g>
    <text x="48" y="38">A</text><text x="26" y="70">B</text><text x="72" y="70">C</text>
  </svg>
  <div class="slide-footer">
    <svg viewBox="0 0 338 56" preserveAspectRatio="none"><polygon points="0,0 338,36 338,56 0,56" fill="var(--navy)"/></svg>
    <span class="dot"></span><span class="wordmark">Velorin</span>
  </div>
</section>

<!-- Slide: content with placeholder -->
<section class="slide" style="top:875px">
  <h2 class="slide-title">TITLE GOES HERE</h2>
  <div class="slide-rule"></div>
  <div class="placeholder">
    <div class="placeholder-icons"><span></span><span></span><span></span><span></span><span></span><span></span></div>
  </div>
  <p class="slide-copy" style="left:202px;top:78px;width:108px">Use this space to describe the visual on the left. Keep the message short, focused and easy to read from the back of the room. Add the key figure, a short comment and a clear next step for the audience. Use this space to describe the visual on the left. Keep the message short, focused and easy to read from the back of the room. Add the key figure, a short comment and a clear next step for the audience.</p>
  <div class="slide-footer">
    <svg viewBox="0 0 338 56" preserveAspectRatio="none"><polygon points="0,0 338,36 338,56 0,56" fill="var(--navy)"/></svg>
    <span class="dot"></span><span class="wordmark">Velorin</span>
  </div>
</section>

</body>
</html>
```